Tarvel Ridge LLC

Need Professional Business cards for New Investment Fund

Target Market(s)

High Quality investors

Industry/Entity Type

Financial

Contact Information for Business Card

Phone Number +1 555 284 6193
Name Pavel Orlinsky
Title Fund Manager
email po@FundTarvel.example
Website www.FundTarvel.example

Colors

Designer to choose colors to be used in the design.

Requirements
Must have
• Must have our Logo and all of the above. Must be made so lettering and loge can be raised

```html
<!DOCTYPE html>
<html lang="en">
<head>
<meta charset="utf-8">
<title>Tarvel Ridge LLC — Business Cards</title>
<link rel="stylesheet" href="https://fonts.googleapis.com/css2?family=Raleway:wght@400;600&family=Teko:wght@500&display=swap">
<style>
  :root {
    --backdrop: #1f1f1f;
    --card-dark: #434f42;
    --accent-green: #58b947;
    --paper: #ffffff;
    --ink-light: #f2f2f2;
  }
  * { margin: 0; padding: 0; box-sizing: border-box; }
  html, body { width: 1200px; height: 900px; overflow: hidden; background: var(--backdrop); }
  .canvas { position: relative; width: 1200px; height: 900px; }
  .card {
    position: absolute; left: 250px; width: 700px; height: 400px; overflow: hidden;
    box-shadow: 0 18px 40px rgba(0,0,0,.55);
  }
  .card-back { top: 35px; background: var(--card-dark); }
  .card-front { top: 465px; background: var(--paper); }

  .brand {
    display: flex; align-items: center; gap: 12px;
    font-family: "Raleway", sans-serif; font-weight: 600; letter-spacing: .04em;
  }
  .brand-mark { display: block; }
  .card-back .brand {
    position: absolute; left: 0; right: 0; top: 168px; justify-content: center;
    color: var(--ink-light); font-size: 40px;
  }
  .card-back .brand-mark { width: 26px; height: 26px; background: var(--accent-green); }
  .accent-bar {
    position: absolute; left: 220px; bottom: 0; width: 260px; height: 12px; background: var(--accent-green);
  }

  .card-front .brand {
    position: absolute; left: 42px; top: 70px; color: var(--card-dark); font-size: 30px;
  }
  .card-front .brand-mark { width: 20px; height: 20px; background: var(--accent-green); }
  .swoosh { position: absolute; inset: 0; width: 700px; height: 400px; }

  .contact-block {
    position: absolute; right: 42px; bottom: 14px; text-align: right;
    font-family: "Raleway", sans-serif; color: var(--ink-light);
  }
  .holder-name {
    font-family: "Teko", sans-serif; font-weight: 500; font-size: 32px; line-height: 1;
    color: var(--accent-green); letter-spacing: .02em;
  }
  .holder-title { font-size: 16px; line-height: 20px; margin-bottom: 6px; }
  .contact-list { list-style: none; }
  .contact-list li {
    display: flex; justify-content: flex-end; align-items: center; gap: 12px;
    font-size: 16px; line-height: 22px;
  }
  .contact-list svg { width: 14px; height: 14px; stroke: var(--accent-green); fill: none; stroke-width: 1.6; }
</style>
</head>
<body>
<main class="canvas">
  <section class="card card-back" aria-label="Card back">
    <div class="brand"><span class="brand-mark"></span>Tarvel Ridge</div>
    <div class="accent-bar"></div>
  </section>

  <section class="card card-front" aria-label="Card front">
    <svg class="swoosh" viewBox="0 0 700 400" aria-hidden="true">
      <path d="M0 225 C160 305 420 295 640 272 C420 290 170 298 0 258 Z" fill="var(--card-dark)"/>
      <path d="M0 298 C250 340 450 280 700 190 L700 400 L0 400 Z" fill="var(--card-dark)"/>
    </svg>
    <div class="brand"><span class="brand-mark"></span>Tarvel Ridge</div>

    <div class="contact-block">
      <p class="holder-name">PAVEL ORLINSKY</p>
      <p class="holder-title">Title Fund Manager</p>
      <ul class="contact-list">
        <li>+1 555 284 6193
          <svg viewBox="0 0 16 16"><path d="M3 2l3 0 1 3-2 1.5c1 2 2.5 3.5 4.5 4.5L11 9l3 1v3c-6 1-12-5-11-11z"/></svg></li>
        <li>po@FundTarvel.example
          <svg viewBox="0 0 16 16"><rect x="1.5" y="3.5" width="13" height="9"/><path d="M1.5 3.5l6.5 5 6.5-5"/></svg></li>
        <li>www.FundTarvel.example
          <svg viewBox="0 0 16 16"><circle cx="8" cy="8" r="6.5"/><path d="M1.5 8h13M8 1.5c-3 3.5-3 9.5 0 13M8 1.5c3 3.5 3 9.5 0 13"/></svg></li>
      </ul>
    </div>
  </section>
</main>
</body>
</html>
```